Flyer für Beteiligungsgesellschaft
Zielgruppe
VORNAL ist eine mittelständische Beteiligungsgesellschaft mit dem Investmentfokus auf Unternehmen in Sondersituationen sowie Unternehmensnachfolgen. Unsere Mitarbeiter verfügen über langjährige internationale Führungserfahrungen in den Bereichen IT, Maschinenbau, Energie, Bau, FMCG sowie bei Beteiligungs- und Beratungsunternehmen. VORNAL ist eine aktive Beteiligungsgesellschaft und stellt selbst das Management oder besetzt Beiratspositionen seiner Beteiligungen, um bei strategischen Fragestellungen sowie dem Tagesgeschäft aktiv zu unterstützen.Zu den bisherigen Investments zählen produzierende Industrie- und Konsumgüterunternehmen, Dienstleistungsunternehmen und Immobilienunternehmen, die sich zum Zeitpunkt des Investments überwiegend in Nachfolge-, Restrukturierungs- oder anderen Sondersituationen befanden.
Aufgabenstellung
A4 dreifach gefaltet

```html
<!DOCTYPE html>
<html lang="de">
<head>
<meta charset="utf-8">
<title>VORNAL Unternehmerbeteiligungen – Flyer</title>
<link href="https://fonts.googleapis.com/css2?family=Source+Sans+3:wght@400;600;700&family=Ubuntu:wght@500;700&display=swap" rel="stylesheet">
<style>
  :root{
    --tan:#d9ab62;
    --blue:#1b97d6;
    --yellow:#eadb22;
    --white:#f1f2f4;
    --ink:#2a2623;
    --divider:#2e2e2e;
    --dark:#1f1f22;
  }
  html,body{margin:0;padding:0;overflow:hidden;background:#fff;}
  .flyer{
    position:relative;width:1200px;height:844px;overflow:hidden;
    background:var(--tan);font-family:"Source Sans 3",Arial,sans-serif;color:var(--ink);
  }
  .backdrop{position:absolute;inset:0;width:1200px;height:844px;}
  .panel-divider{position:absolute;top:0;width:2px;height:844px;background:var(--divider);}
  .panel-divider.first{left:390px;}
  .panel-divider.second{left:797px;}

  .company-heading{
    position:absolute;left:31px;top:376px;margin:0;
    font-weight:700;font-size:39px;letter-spacing:-0.5px;color:var(--blue);line-height:1;
  }
  .company-text{
    position:absolute;left:31px;top:420px;width:342px;margin:0;
    font-size:15.2px;line-height:18.9px;text-align:justify;hyphens:auto;
  }

  .contact{
    position:absolute;left:428px;top:691px;margin:0;
    font-size:15px;line-height:20.6px;font-style:normal;
  }
  .contact .gap{display:block;height:20.6px;}

  .brand-band{
    position:absolute;left:882px;top:86px;width:305px;height:70px;background:var(--dark);
    display:flex;align-items:center;gap:18px;padding-left:16px;box-sizing:border-box;
  }
  .brand-band .dot{width:34px;height:34px;border-radius:50%;background:var(--blue);}
  .brand-band .name{
    font-weight:700;font-size:34px;letter-spacing:13px;color:var(--blue);
  }

  .brand-title{
    position:absolute;left:822px;top:326px;margin:0;
    font-weight:700;font-size:72px;letter-spacing:8px;color:var(--blue);line-height:1;
  }
  .brand-sub{
    position:absolute;right:34px;top:413px;margin:0;font-size:13.5px;color:var(--ink);
  }
  .brand-rule{position:absolute;left:822px;top:434px;width:347px;height:4px;background:var(--blue);}

  .claims{position:absolute;left:826px;top:483px;margin:0;padding:0;list-style:none;width:345px;}
  .claims li{
    position:relative;padding-left:45px;font-family:"Ubuntu",Arial,sans-serif;font-weight:700;
    font-size:18.6px;line-height:25.8px;color:var(--ink);
  }
  .claims li + li{margin-top:54px;padding-left:42px;}
  .claims li::before{
    content:"";position:absolute;left:3px;top:7px;width:13px;height:13px;
    background:var(--ink);transform:rotate(45deg);
  }
</style>
</head>
<body>
<div class="flyer">
  <svg class="backdrop" viewBox="0 0 1200 844" xmlns="http://www.w3.org/2000/svg">
    <defs>
      <linearGradient id="cityTones" x1="0" y1="0" x2="0" y2="1">
        <stop offset="0" stop-color="#6c7f98"/>
        <stop offset="0.25" stop-color="#5b5e68"/>
        <stop offset="0.55" stop-color="#6d4a40"/>
        <stop offset="1" stop-color="#343a45"/>
      </linearGradient>
    </defs>
    <!-- city skyline area -->
    <path d="M0,0 H1200 V318 C1080,280 950,230 800,256 C690,276 560,372 391,376 C250,380 110,310 0,228 Z"
          fill="url(#cityTones)" role="img" aria-label="Luftaufnahme der Hamburger Innenstadt in der Abenddämmerung"/>
    <!-- wave bands under the city -->
    <path d="M0,240 C110,322 250,392 391,388 C560,384 690,288 800,270 C950,244 1080,294 1200,332"
          fill="none" stroke="var(--white)" stroke-width="18"/>
    <path d="M0,234 C110,316 250,384 391,380 C560,376 690,280 800,262 C950,236 1080,286 1200,324"
          fill="none" stroke="var(--blue)" stroke-width="5"/>
    <path d="M0,246 C110,328 250,396 391,392 C560,388 690,292 800,274 C950,248 1080,298 1200,336"
          fill="none" stroke="var(--yellow)" stroke-width="3"/>
    <!-- tan below bands -->
    <path d="M0,250 C110,332 250,400 391,396 C560,392 690,296 800,278 C950,252 1080,302 1200,340 V844 H0 Z"
          fill="var(--tan)"/>
    <!-- location map -->
    <path d="M422,401 C560,388 690,320 774,294 V666 H422 Z"
          fill="#e7e3da" stroke="var(--blue)" stroke-width="3.5"
          role="img" aria-label="Stadtplan mit dem Standort des Büros in der Hamburger Innenstadt"/>
    <!-- bottom waves -->
    <path d="M0,742 C90,800 230,836 350,844 H0 Z" fill="var(--white)"/>
    <path d="M0,736 C90,794 230,832 350,844" fill="none" stroke="var(--yellow)" stroke-width="3"/>
    <path d="M700,844 C780,802 900,742 1000,750 C1080,756 1150,800 1200,832 V844 Z" fill="var(--white)"/>
    <path d="M700,840 C780,798 900,738 1000,746 C1080,752 1150,796 1200,828" fill="none" stroke="var(--blue)" stroke-width="4"/>
    <path d="M690,844 C770,806 890,748 995,755" fill="none" stroke="var(--yellow)" stroke-width="2.5"/>
  </svg>

  <div class="panel-divider first"></div>
  <div class="panel-divider second"></div>

  <h2 class="company-heading">UNTERNEHMEN</h2>
  <p class="company-text">VORNAL ist eine mittelständische Beteiligungsgesellschaft mit dem Investmentfokus auf Unternehmen in Sondersituationen sowie Unternehmensnachfolgen. Unsere Mitarbeiter verfügen über langjährige internationale Führungserfahrungen in den Bereichen IT, Maschinenbau, Energie, Bau, FMCG sowie bei Beteiligungs- und Beratungsunternehmen. VORNAL ist eine aktive Beteiligungsgesellschaft und stellt selbst das Management oder besetzt Beiratspositionen seiner Beteiligungen, um bei strategischen Fragestellungen sowie dem Tagesgeschäft aktiv zu unterstützen.Zu den bisherigen Investments zählen produzierende Industrie- und Konsumgüterunternehmen, Dienstleistungsunternehmen und Immobilienunternehmen, die sich zum Zeitpunkt des Investments überwiegend in Nachfolge-, Restrukturierungs- oder anderen Sondersituationen befanden.</p>

  <address class="contact">
    VORNAL Unternehmerbeteiligungen GmbH<br>
    Lindenhof-Passage<br>
    Lindenstraße 18<br>
    D-20355 Hamburg<br>
    <span class="gap"></span>
    Telefon +49 40 7720150<br>
    Fax +49 40 7720159
  </address>

  <div class="brand-band"><span class="dot"></span><span class="name">VORNAL</span></div>

  <h1 class="brand-title">VORNAL</h1>
  <p class="brand-sub">Unternehmerbeteiligungen GmbH</p>
  <div class="brand-rule"></div>

  <ul class="claims">
    <li>Der Unternehmer trägt weiterhin Verantwortung und behält weiterhin Einfluss auf sein Unternehmen!</li>
    <li>Wir sind „Mitunternehmer“ keine Finanzinvestoren...</li>
  </ul>
</div>
</body>
</html>
```